Home Page Design

Please see design brief attached. Concept here: sketchboard[dot]io/file/qWm83LzpR7cvXuNtYa2KhE/Brindlemoor---Landing-Page?node-id=0%3A1&t=PKr92mvnQsD4xTcZ-1

Industry/Entity Type

Wedding

Number of Pages Required

1 page

Font styles to use
Serif
Sans Serif
Decorative
Script

Colors
A7469A
B969AE
D3A5CF
EDDBEB
F8F0F9
6B429C
8869AF
B7A5CE
E3DAEB
F3F0F8

Requirements
Must have
• Please see attached PDF
Nice to have
• Please see attached PDF
Should not have
• Please see attached PDF

```html
<!DOCTYPE html>
<html lang="en">
<head>
<meta charset="utf-8">
<title>Brindlemoor — Wedding Vendors Landing Page</title>
<link href="https://fonts.googleapis.com/css2?family=Great+Vibes&family=Yesteryear&family=Roboto+Slab:wght@300;400;500;700&family=Roboto:wght@400;500&display=swap" rel="stylesheet">
<style>
:root{
  --magenta:#e3157f;
  --magenta-soft:#f7d3e6;
  --plum:#6c2a7e;
  --plum-deep:#4b1d5a;
  --ink:#2d2d2d;
  --line:#d9d9d9;
  --grey:#f2f2f2;
  --white:#fff;
}
*{box-sizing:border-box;margin:0;padding:0}
html,body{width:1200px;height:5038px;overflow:hidden}
body{font-family:"Roboto Slab",serif;color:var(--ink);background:var(--white)}
.page{position:relative;width:1200px;height:5038px;overflow:hidden}
.abs{position:absolute}
.script-bold{font-family:"Yesteryear",cursive;color:var(--magenta);font-weight:400}
.btn{display:inline-flex;align-items:center;justify-content:center;font-family:"Roboto Slab",serif;font-size:12px;color:#fff;border-radius:3px}
.btn-plum{background:var(--plum)}
.btn-pink{background:var(--magenta)}

.topbar{top:0;left:0;width:1200px;height:31px;background:var(--plum)}
.topbar .contact{position:absolute;top:8px;font-size:12px;color:#fff;font-family:"Roboto",sans-serif;display:flex;align-items:center;gap:6px}
.social{position:absolute;top:0;width:28px;height:31px;display:flex;align-items:center;justify-content:center}
.social span{width:10px;height:10px;border-radius:50%;background:#c79bd0}
.social.active{background:var(--magenta)}
.social.active span{background:#fff}
.nav{top:31px;left:0;width:1200px;height:80px;background:#fff}
.nav a{position:absolute;top:30px;font-size:12px;color:var(--plum);text-decoration:none}
.nav a.cta{border-bottom:1px solid var(--magenta)}
.logo-box{top:0;left:129px;width:238px;height:125px;background:#fff;border-left:5px solid var(--magenta);border-bottom:5px solid var(--magenta);box-shadow:0 2px 6px rgba(0,0,0,.15);display:flex;flex-direction:column;align-items:center;justify-content:center;gap:8px}
.logo-name{font-family:"Roboto Slab",serif;font-size:26px;color:var(--plum);font-weight:400}
.logo-tag{font-size:8px;color:var(--magenta);letter-spacing:.5px}

.hero-photo{top:111px;left:0;width:1200px;height:520px;background:linear-gradient(120deg,#3d2b35 0%,#5a3f4c 40%,#2f2a2e 70%,#4e3946 100%);clip-path:polygon(0 0,100% 0,100% 420px,50% 510px,0 420px)}
.hero-title{top:300px;left:0;width:1200px;text-align:center;font-size:38px}
.hero-sub{top:354px;left:0;width:1200px;text-align:center;color:#fff;font-size:12px}
.select{top:392px;height:28px;background:#fff;border-radius:2px;font-size:10px;color:#777;padding:0 10px;display:flex;align-items:center;justify-content:space-between}
.dots{top:562px;left:553px;display:flex;gap:12px}
.dots span{width:12px;height:12px;border:2px solid #fff;border-radius:50%}
.dots span.on{background:var(--magenta);border-color:var(--magenta)}

.stat{top:718px;width:186px;text-align:center}
.stat svg{display:block;margin:0 auto}
.stat .num{font-size:40px;font-weight:700;color:var(--magenta);line-height:1;margin-top:14px}
.stat .label{font-size:13px;color:#555;margin-top:6px}
.stat .rule{height:2px;background:var(--line);margin-top:18px}

.sec-title{left:0;width:1200px;display:flex;align-items:center;justify-content:center;gap:18px}
.sec-title .dash{width:40px;height:1px;background:var(--magenta);position:relative}
.sec-title .dash::after{content:"";position:absolute;top:-2px;width:5px;height:5px;border-radius:50%;background:var(--magenta)}
.sec-title .dash.l::after{right:0}
.sec-title .dash.r::after{left:0}
.sec-title h2{font-family:"Great Vibes",cursive;font-weight:400;color:var(--magenta);font-size:46px;line-height:1}

.grey-band{left:0;width:1200px;background:var(--grey)}
.grid{top:1104px;left:160px;display:grid;grid-template-columns:repeat(3,270px);column-gap:33px;row-gap:41px}
.card{width:270px;height:303px;background:#fff;border:1px solid #e2e2e2;border-bottom:3px solid var(--plum);box-shadow:0 1px 4px rgba(0,0,0,.08);position:relative;text-align:center}
.card .photo{margin:5px 5px 0;height:161px}
.card h3{font-size:16px;font-weight:500;color:var(--plum);margin-top:18px}
.card .loc{font-size:11px;color:#444;margin-top:6px;display:flex;justify-content:center;align-items:center;gap:5px}
.card .price{font-size:11px;color:var(--magenta);margin-top:7px}
.card .bar{position:absolute;left:0;right:0;bottom:0;height:37px;border-top:1px solid #e4e4e4;display:flex}
.card .bar .more{width:150px;display:flex;align-items:center;justify-content:center;font-size:12px;color:var(--plum)}
.card .bar .ico{width:60px;display:flex;align-items:center;justify-content:center;border-left:1px solid #e4e4e4}
.card .bar .active{background:var(--magenta);color:#fff}

.quote-ico{top:2050px;left:325px;width:58px;height:58px;border-radius:50%;background:var(--magenta);display:flex;align-items:center;justify-content:center}
.testi-head{top:2125px;left:150px;width:408px;text-align:center;font-size:16px;font-weight:500;line-height:23px}
.testi-body{top:2180px;left:150px;width:408px;text-align:center;font-size:11px;color:#444;line-height:17px}
.stars{top:2254px;left:0;width:708px;text-align:center;color:#e8c514;font-size:16px;letter-spacing:3px}
.testi-name{top:2286px;left:0;width:708px;text-align:center;font-size:12px;color:var(--magenta);font-weight:500}
.testi-role{top:2303px;left:0;width:708px;text-align:center;font-size:9px;color:#555}
.arrow{width:24px;height:24px;border-radius:50%;background:#efe4f1;display:flex;align-items:center;justify-content:center;color:var(--plum);font-size:14px}
.promo-box{border:1px solid rgba(255,255,255,.35);text-align:center}

.feature-list{top:2574px;left:621px;width:430px}
.feature-list h4{font-size:14px;font-weight:500;margin-bottom:18px}
.feature-list li{list-style:none;display:flex;gap:8px;font-size:11px;line-height:17px;color:#333;margin-bottom:17px}
.feature-list li i{flex:none;width:10px;height:10px;border-radius:50%;background:var(--magenta);margin-top:3px;position:relative}
.feature-list li i::after{content:"";position:absolute;left:3px;top:2px;border-left:4px solid #fff;border-top:3px solid transparent;border-bottom:3px solid transparent}

.step{top:3170px;width:266px;height:236px;background:#fff;border:1px solid #e2e2e2;border-bottom:3px solid var(--plum);box-shadow:0 1px 4px rgba(0,0,0,.08);text-align:center;padding:50px 22px 0}
.step h3{font-size:15px;font-weight:500;color:var(--plum);line-height:20px}
.step p{font-size:11px;color:#555;line-height:17px;margin-top:10px}
.step-num{top:3147px;width:48px;height:48px;border-radius:50%;background:var(--plum);color:#fff;font-size:18px;display:flex;align-items:center;justify-content:center}

.slide{top:3851px;width:168px;height:288px;background:#fff;border:1px solid #e2e2e2;border-bottom:3px solid var(--plum);text-align:center}
.slide .photo{margin:4px 4px 0;height:142px}
.slide p{font-size:12px;color:var(--plum);font-weight:500;line-height:18px;margin:20px 14px 0}
.slide .btn{margin-top:12px;width:108px;height:28px}

.sub-input{top:4373px;left:500px;width:250px;height:32px;border:1px solid #ddd;font-size:11px;color:#aaa;padding:0 12px;display:flex;align-items:center}

.footer-bg{top:4494px;left:0;width:1200px;height:512px;background:linear-gradient(180deg,#2a2230 0%,#1c181e 60%,#231c26 100%)}
.fcol{color:#fff;font-size:11px}
.fcol h5{font-size:14px;font-weight:400;color:var(--magenta);margin-bottom:6px}
.fcol li{list-style:none;line-height:23px}
.bottombar{top:5006px;left:0;width:1200px;height:32px;background:var(--plum);color:#fff;font-size:11px}
</style>
</head>
<body>
<div class="page">

  <div class="abs topbar">
    <div class="contact" style="left:630px">
      <svg width="11" height="11" viewBox="0 0 24 24"><path fill="#e77cb4" d="M6.6 10.8a15 15 0 0 0 6.6 6.6l2.2-2.2a1 1 0 0 1 1-.25 11.4 11.4 0 0 0 3.6.57 1 1 0 0 1 1 1V20a1 1 0 0 1-1 1A17 17 0 0 1 3 4a1 1 0 0 1 1-1h3.5a1 1 0 0 1 1 1c0 1.25.2 2.45.57 3.57a1 1 0 0 1-.25 1z"/></svg>
      +123-555-0142</div>
    <div class="contact" style="left:778px">
      <svg width="12" height="10" viewBox="0 0 24 18"><rect x="1" y="1" width="22" height="16" rx="2" fill="none" stroke="#e77cb4" stroke-width="2"/><path d="M1 2l11 8 11-8" fill="none" stroke="#e77cb4" stroke-width="2"/></svg>
      info@brindlemoor.com</div>
    <div class="social" style="left:970px"><span></span></div>
    <div class="social active" style="left:1002px"><span></span></div>
    <div class="social" style="left:1034px"><span></span></div>
  </div>

  <nav class="abs nav">
    <a href="#" style="left:620px">Vendors</a>
    <a href="#" style="left:703px">Venues</a>
    <a href="#" style="left:778px">Blogs</a>
    <a href="#" style="left:847px">Sign in or Register</a>
    <a href="#" class="cta" style="left:976px">Join as a Vendor</a>
  </nav>
  <div class="abs logo-box">
    <div class="logo-name">Brindlemoor</div>
    <div class="logo-tag">WEDDING VENDORS. INSTANTLY BOOKED!</div>
  </div>

  <div class="abs hero-photo" role="img" aria-label="Photo of a bride and groom embracing outdoors among flowers"></div>
  <h1 class="abs hero-title script-bold">Meet Your Wedding Vendor Team.</h1>
  <p class="abs hero-sub">Find and book the best wedding vendors for your special day</p>
  <div class="abs select" style="left:342px;width:199px">Select Vendor type <span>▾</span></div>
  <div class="abs select" style="left:549px;width:199px">Location <span>▾</span></div>
  <div class="abs btn btn-pink" style="top:392px;left:758px;width:96px;height:28px">Search</div>
  <div class="abs dots"><span></span><span class="on"></span><span></span><span></span></div>
  <svg class="abs" style="top:590px;left:0" width="1200" height="56" viewBox="0 0 1200 56"><polygon points="350,8 600,36 850,8 600,52" fill="var(--plum)"/></svg>

  <div class="abs stat" style="left:173px">
    <svg width="38" height="38" viewBox="0 0 40 40" fill="none" stroke="#333" stroke-width="2"><path d="M6 38V16a14 14 0 0 1 28 0v22M13 38V17a7 7 0 0 1 14 0v21M3 38h34"/></svg>
    <div class="num">700</div><div class="label">Venues</div><div class="rule"></div>
  </div>
  <div class="abs stat" style="left:395px">
    <svg width="38" height="38" viewBox="0 0 40 40" fill="none" stroke="#333" stroke-width="2"><path d="M5 14l3-10h24l3 10zM5 14v4a5 5 0 0 0 10 0 5 5 0 0 0 10 0 5 5 0 0 0 10 0v-4M7 22v15h26V22M16 37v-9h8v9"/></svg>
    <div class="num">1500</div><div class="label">Vendors</div><div class="rule"></div>
  </div>
  <div class="abs stat" style="left:616px">
    <svg width="38" height="38" viewBox="0 0 40 40" fill="none" stroke="#333" stroke-width="2"><circle cx="14" cy="24" r="9"/><circle cx="26" cy="24" r="9"/><path d="M20 4l3 4-3 4-3-4z"/></svg>
    <div class="num">500</div><div class="label">Weddings Booked</div><div class="rule"></div>
  </div>
  <div class="abs stat" style="left:839px">
    <svg width="38" height="38" viewBox="0 0 40 40" fill="none" stroke="#333" stroke-width="2"><circle cx="22" cy="11" r="8"/><path d="M22 6v10M19.5 8.5h4a1.5 1.5 0 0 1 0 3h-3a1.5 1.5 0 0 0 0 3h4M3 28h8l8 4h6l10-6M11 28l6-4h6"/></svg>
    <div class="num">$7,680</div><div class="label">Averaged Saved</div><div class="rule"></div>
  </div>

  <div class="abs grey-band" style="top:918px;height:958px"></div>
  <div class="abs sec-title" style="top:1020px"><span class="dash l"></span><h2>Explore our Marketplace</h2><span class="dash r"></span></div>

  <div class="abs grid">
    <div class="card">
      <div class="photo" role="img" aria-label="Photographer shooting a wedding couple" style="background:linear-gradient(135deg,#c9b8ad,#7d6f6a)"></div>
      <h3>Photographers</h3>
      <div class="loc"><svg width="9" height="12" viewBox="0 0 10 14"><path d="M5 0a5 5 0 0 0-5 5c0 4 5 9 5 9s5-5 5-9a5 5 0 0 0-5-5zm0 7a2 2 0 1 1 0-4 2 2 0 0 1 0 4z" fill="var(--plum)"/></svg>Location here</div>
      <div class="price">Starting Price: $2000</div>
      <div class="bar"><div class="more">Read More</div><div class="ico active"><svg width="16" height="16" viewBox="0 0 24 24" fill="none" stroke="#fff" stroke-width="2"><path d="M20 11a8 8 0 0 0-14-5L4 8M4 4v4h4M4 13a8 8 0 0 0 14 5l2-2M20 20v-4h-4"/></svg></div><div class="ico"><svg width="16" height="14" viewBox="0 0 24 22" fill="none" stroke="var(--plum)" stroke-width="2"><path d="M12 20S2 14 2 7.5A5 5 0 0 1 12 5a5 5 0 0 1 10 2.5C22 14 12 20 12 20z"/></svg></div></div>
    </div>
    <div class="card">
      <div class="photo" role="img" aria-label="DJ mixing console under red stage lights" style="background:linear-gradient(135deg,#7a1a22,#2a1214)"></div>
      <h3>DJs</h3>
      <div class="loc"><svg width="9" height="12" viewBox="0 0 10 14"><path d="M5 0a5 5 0 0 0-5 5c0 4 5 9 5 9s5-5 5-9a5 5 0 0 0-5-5zm0 7a2 2 0 1 1 0-4 2 2 0 0 1 0 4z" fill="var(--plum)"/></svg>Location here</div>
      <div class="price">Starting Price: $2000</div>
      <div class="bar"><div class="more">Read More</div><div class="ico"><svg width="16" height="16" viewBox="0 0 24 24" fill="none" stroke="var(--plum)" stroke-width="2"><path d="M20 11a8 8 0 0 0-14-5L4 8M4 4v4h4M4 13a8 8 0 0 0 14 5l2-2M20 20v-4h-4"/></svg></div><div class="ico"><svg width="16" height="14" viewBox="0 0 24 22" fill="none" stroke="var(--plum)" stroke-width="2"><path d="M12 20S2 14 2 7.5A5 5 0 0 1 12 5a5 5 0 0 1 10 2.5C22 14 12 20 12 20z"/></svg></div></div>
    </div>
    <div class="card">
      <div class="photo" role="img" aria-label="Bride having makeup applied" style="background:linear-gradient(135deg,#e6c9a8,#b68a62)"></div>
      <h3>Hair &amp; Makeup</h3>
      <div class="loc"><svg width="9" height="12" viewBox="0 0 10 14"><path d="M5 0a5 5 0 0 0-5 5c0 4 5 9 5 9s5-5 5-9a5 5 0 0 0-5-5zm0 7a2 2 0 1 1 0-4 2 2 0 0 1 0 4z" fill="var(--plum)"/></svg>Location here</div>
      <div class="price">Starting Price: $2000</div>
      <div class="bar"><div class="more">Read More</div><div class="ico"><svg width="16" height="16" viewBox="0 0 24 24" fill="none" stroke="var(--plum)" stroke-width="2"><path d="M20 11a8 8 0 0 0-14-5L4 8M4 4v4h4M4 13a8 8 0 0 0 14 5l2-2M20 20v-4h-4"/></svg></div><div class="ico"><svg width="16" height="14" viewBox="0 0 24 22" fill="none" stroke="var(--plum)" stroke-width="2"><path d="M12 20S2 14 2 7.5A5 5 0 0 1 12 5a5 5 0 0 1 10 2.5C22 14 12 20 12 20z"/></svg></div></div>
    </div>
    <div class="card">
      <div class="photo" role="img" aria-label="Wedding planner meeting with a bride beside a gown" style="background:linear-gradient(135deg,#e9e4df,#a9a19a)"></div>
      <h3>Planners</h3>
      <div class="loc"><svg width="9" height="12" viewBox="0 0 10 14"><path d="M5 0a5 5 0 0 0-5 5c0 4 5 9 5 9s5-5 5-9a5 5 0 0 0-5-5zm0 7a2 2 0 1 1 0-4 2 2 0 0 1 0 4z" fill="var(--plum)"/></svg>Location here</div>
      <div class="price">Starting Price: $2000</div>
      <div class="bar"><div class="more">Read More</div><div class="ico"><svg width="16" height="16" viewBox="0 0 24 24" fill="none" stroke="var(--plum)" stroke-width="2"><path d="M20 11a8 8 0 0 0-14-5L4 8M4 4v4h4M4 13a8 8 0 0 0 14 5l2-2M20 20v-4h-4"/></svg></div><div class="ico"><svg width="16" height="14" viewBox="0 0 24 22" fill="none" stroke="var(--plum)" stroke-width="2"><path d="M12 20S2 14 2 7.5A5 5 0 0 1 12 5a5 5 0 0 1 10 2.5C22 14 12 20 12 20z"/></svg></div></div>
    </div>
    <div class="card">
      <div class="photo" role="img" aria-label="Catering buffet with stacked plates" style="background:linear-gradient(135deg,#f1ede8,#8e8a84)"></div>
      <h3>Caterers</h3>
      <div class="loc"><svg width="9" height="12" viewBox="0 0 10 14"><path d="M5 0a5 5 0 0 0-5 5c0 4 5 9 5 9s5-5 5-9a5 5 0 0 0-5-5zm0 7a2 2 0 1 1 0-4 2 2 0 0 1 0 4z" fill="var(--plum)"/></svg>Location here</div>
      <div class="price">Starting Price: $2000</div>
      <div class="bar"><div class="more">Read More</div><div class="ico"><svg width="16" height="16" viewBox="0 0 24 24" fill="none" stroke="var(--plum)" stroke-width="2"><path d="M20 11a8 8 0 0 0-14-5L4 8M4 4v4h4M4 13a8 8 0 0 0 14 5l2-2M20 20v-4h-4"/></svg></div><div class="ico"><svg width="16" height="14" viewBox="0 0 24 22" fill="none" stroke="var(--plum)" stroke-width="2"><path d="M12 20S2 14 2 7.5A5 5 0 0 1 12 5a5 5 0 0 1 10 2.5C22 14 12 20 12 20z"/></svg></div></div>
    </div>
    <div class="card">
      <div class="photo" role="img" aria-label="Florist arranging a bouquet of roses" style="background:linear-gradient(135deg,#c76b7a,#4f6b3e)"></div>
      <h3>Florists</h3>
      <div class="loc"><svg width="9" height="12" viewBox="0 0 10 14"><path d="M5 0a5 5 0 0 0-5 5c0 4 5 9 5 9s5-5 5-9a5 5 0 0 0-5-5zm0 7a2 2 0 1 1 0-4 2 2 0 0 1 0 4z" fill="var(--plum)"/></svg>Location here</div>
      <div class="price">Starting Price: $2000</div>
      <div class="bar"><div class="more active">Read More</div><div class="ico"><svg width="16" height="16" viewBox="0 0 24 24" fill="none" stroke="var(--plum)" stroke-width="2"><path d="M20 11a8 8 0 0 0-14-5L4 8M4 4v4h4M4 13a8 8 0 0 0 14 5l2-2M20 20v-4h-4"/></svg></div><div class="ico"><svg width="16" height="14" viewBox="0 0 24 22" fill="none" stroke="var(--plum)" stroke-width="2"><path d="M12 20S2 14 2 7.5A5 5 0 0 1 12 5a5 5 0 0 1 10 2.5C22 14 12 20 12 20z"/></svg></div></div>
    </div>
  </div>
  <div class="abs btn btn-plum" style="top:1803px;left:555px;width:90px;height:32px">View All</div>

  <div class="abs" style="top:1866px;left:0;width:1200px;height:576px;background:#fff"></div>
  <div class="abs" role="img" aria-label="Bride holding a pink rose bouquet, tinted purple" style="top:1866px;left:600px;width:600px;height:576px;background:linear-gradient(135deg,#5c2f67,#7a3f7c 50%,#4a2456);clip-path:polygon(0 60px,100% 0,100% 547px,0 576px)"></div>
  <div class="abs sec-title" style="top:1985px;width:708px"><span class="dash l"></span><h2>Testimonials</h2><span class="dash r"></span></div>
  <div class="abs quote-ico"><svg width="26" height="22" viewBox="0 0 26 22" fill="#fff"><path d="M0 12C0 5 4 1 10 0v4c-3 1-5 3-5 6h5v12H0zM14 12c0-7 4-11 10-12v4c-3 1-5 3-5 6h5v12H14z"/></svg></div>
  <div class="abs testi-head">This is a great place to consider<br>for any event</div>
  <p class="abs testi-body">Lorem Ipsum is simply dummy text of the printing and typesetting industry. Lorem Ipsum has been the industry's standard dummy text ever since the 1500s, when an unknown printer took...</p>
  <div class="abs stars">★★★★★</div>
  <div class="abs testi-name">John C.</div>
  <div class="abs testi-role">CEO, Harlow Group</div>
  <div class="abs arrow" style="top:2295px;left:228px">‹</div>
  <div class="abs arrow" style="top:2295px;left:457px">›</div>

  <div class="abs promo-box" style="top:2058px;left:651px;width:369px;height:228px">
    <div class="script-bold" style="margin-top:32px;font-size:26px;line-height:34px">Because life is too short to<br>wait for vendors to reply</div>
    <p style="color:#fff;font-size:11px;line-height:19px;margin-top:14px">Focus on enjoying your wedding! Don't get tied<br>into endless negotiations and emails</p>
    <div class="btn btn-plum" style="margin-top:22px;width:105px;height:31px">Explore</div>
  </div>

  <div class="abs grey-band" style="top:2442px;height:489px;clip-path:polygon(0 0,100% 0,100% 430px,50% 489px,0 430px)"></div>
  <div class="abs sec-title" style="top:2474px"><span class="dash l"></span><h2>Features / Benefits</h2><span class="dash r"></span></div>
  <div class="abs" role="img" aria-label="Wedding stage with a pink floral wall and a golden sofa" style="top:2558px;left:127px;width:426px;height:305px;border:4px solid #fff;box-shadow:0 0 0 1px var(--magenta-soft);background:linear-gradient(135deg,#e8c6ea,#c77fc4 50%,#f2e3f0)"></div>
  <div class="abs feature-list">
    <h4>List of features for the platform:</h4>
    <ul>
      <li><i></i>User-friendly and intuitive booking process. Each vendor lists multiple packages for instant purchase (similar to Gigloom or Staynest)</li>
      <li><i></i>Detailed information about each vendor and venue, including pictures and descriptions</li>
      <li><i></i>Ability to view and select vendors and venues based on location, price, and other criteria</li>
      <li><i></i>Multiple online payment options, including credit card, bank transfers, and Flexible payment plans / financing options</li>
    </ul>
  </div>
  <div class="abs btn btn-pink" style="top:2822px;left:621px;width:124px;height:31px">Explore More</div>

  <div class="abs sec-title" style="top:3076px"><span class="dash l"></span><h2>How It Works?</h2><span class="dash r"></span></div>
  <div class="abs step" style="left:178px"><h3>Browse Top Vendors</h3><p>Lorem ipsum dolor sit amet, consectetur adipiscing elit. Suspendisse ac bibendum nibh. Nulla tempor nibh ex, ac sodales augue tempus sit amet. Morbi at turpis auctor, venenatis ipsum...</p></div>
  <div class="abs step" style="left:467px"><h3>Instantly Book with<br>Pre-negotiated Prices</h3><p>Lorem ipsum dolor sit amet, consectetur adipiscing elit. Suspendisse ac bibendum nibh. Nulla tempor nibh ex, ac sodales augue tempus sit amet. Morbi at turpis auctor, venenatis ipsum...</p></div>
  <div class="abs step" style="left:756px"><h3>Pay Over Time</h3><p>Lorem ipsum dolor sit amet, consectetur adipiscing elit. Suspendisse ac bibendum nibh. Nulla tempor nibh ex, ac sodales augue tempus sit amet. Morbi at turpis auctor, venenatis ipsum...</p></div>
  <div class="abs step-num" style="left:287px">1</div>
  <div class="abs step-num" style="left:576px">2</div>
  <div class="abs step-num" style="left:865px">3</div>

  <h3 class="abs" style="top:3496px;left:178px;width:420px;font-size:17px;font-weight:500;color:var(--plum);line-height:22px">Brindlesure! - Because life happens. All your bookings are fully insured</h3>
  <p class="abs" style="top:3556px;left:178px;width:420px;font-size:11px;color:#555;line-height:17px">Lorem ipsum dolor sit amet, consectetur adipiscing elit. Suspendisse ac bibendum nibh. Nulla tempor nibh ex, ac sodales augue tempus sit amet. Morbi at turpis auctor, venenatis ipsum...</p>
  <div class="abs" role="img" aria-label="Wedding invitation cards and a couple photo collage" style="top:3461px;left:668px;width:352px;height:183px;border:4px solid #fff;box-shadow:0 0 0 1px var(--magenta-soft);background:linear-gradient(135deg,#6f5a63,#d8d2ce 50%,#8ea0b4)"></div>
  <div class="abs" style="top:3514px;left:804px;width:80px;height:80px;border-radius:50%;background:var(--plum);display:flex;align-items:center;justify-content:center">
    <svg width="36" height="34" viewBox="0 0 36 34" fill="none" stroke="#fff" stroke-width="2"><rect x="2" y="5" width="32" height="27" rx="3"/><path d="M2 12h32M10 2v6M26 2v6"/><g fill="#fff" stroke="none"><rect x="8" y="16" width="4" height="4"/><rect x="16" y="16" width="4" height="4"/><rect x="24" y="16" width="4" height="4"/><rect x="8" y="24" width="4" height="4"/><rect x="16" y="24" width="4" height="4"/></g></svg>
  </div>

  <div class="abs grey-band" style="top:3732px;height:518px"></div>
  <div class="abs" role="img" aria-label="Purple-tinted photo of wedding details" style="top:3732px;left:0;width:600px;height:518px;background:linear-gradient(135deg,#3e1d4b,#5f2e6c 50%,#3a1a44);clip-path:polygon(0 45px,100% 0,100% 518px,0 480px)"></div>
  <div class="abs promo-box" style="top:3850px;left:182px;width:369px;height:292px">
    <svg style="margin-top:26px" width="40" height="46" viewBox="0 0 40 46"><path d="M4 2h24l10 10v32H4z" fill="none" stroke="var(--magenta)" stroke-width="2"/><rect x="0" y="16" width="28" height="14" fill="var(--magenta)"/><text x="14" y="27" text-anchor="middle" font-family="Roboto" font-size="10" fill="#fff">PDF</text></svg>
    <div class="script-bold" style="margin-top:14px;font-size:27px;line-height:33px;color:#fff">Download our free PDF<br>and start down the<br>road to saving money</div>
    <div class="btn btn-pink" style="margin-top:20px;width:127px;height:27px">Download PDF</div>
  </div>
  <div class="abs slide" style="left:668px">
    <div class="photo" role="img" aria-label="Two gold wedding rings on a rose" style="background:linear-gradient(135deg,#f3e6d4,#c9a878)"></div>
    <p>Lorem Ipsum is simply dummy text industry.</p>
    <div class="btn btn-pink">Book Today!</div>
  </div>
  <div class="abs slide" style="left:852px">
    <div class="photo" role="img" aria-label="Outdoor wedding reception tent lit at dusk" style="background:linear-gradient(180deg,#6d9bd0,#c7a15c 60%,#3b4a2c)"></div>
    <p>Lorem Ipsum is simply dummy text industry.</p>
    <div class="btn btn-plum">Book Today!</div>
  </div>
  <div class="abs arrow" style="top:3976px;left:625px">‹</div>
  <div class="abs arrow" style="top:3976px;left:1039px">›</div>

  <div class="abs" style="top:4304px;left:353px;width:118px;height:118px;border-radius:50%;background:var(--plum);display:flex;align-items:center;justify-content:center">
    <svg width="64" height="52" viewBox="0 0 64 52" fill="none" stroke="#fff" stroke-width="2.5"><path d="M6 24L58 4 46 48 30 34zM30 34l28-30M30 34v14l8-8"/><path d="M2 38h12M6 44h10"/></svg>
  </div>
  <h3 class="abs" style="top:4312px;left:500px;font-size:21px;font-weight:500;color:var(--magenta)">Your Success Is Our Success</h3>
  <p class="abs" style="top:4342px;left:500px;font-size:11px;color:#444">Subscribe and Join Our Network</p>
  <div class="abs sub-input">name@email.com</div>
  <div class="abs btn btn-plum" style="top:4373px;left:754px;width:90px;height:32px">Sign Up</div>

  <svg class="abs" style="top:4458px;left:0" width="1200" height="40" viewBox="0 0 1200 40"><polygon points="360,36 600,0 840,36" fill="var(--plum)"/></svg>
  <div class="abs footer-bg" role="img" aria-label="Dark-toned wedding reception photo"></div>
  <div class="abs" style="top:4556px;left:0;width:1200px;text-align:center">
    <div class="logo-name" style="color:#fff">Brindlemoor</div>
    <div class="logo-tag" style="margin-top:8px">WEDDING VENDORS. INSTANTLY BOOKED!</div>
  </div>
  <div class="abs fcol" style="top:4654px;left:125px"><h5>Local Services</h5><ul><li>Wedding Photographers</li><li>Wedding DJs</li><li>Wedding Hair &amp; Makeup</li><li>Wedding Planners</li><li>Wedding Caterers</li></ul></div>
  <div class="abs fcol" style="top:4683px;left:371px"><ul><li>Wedding Florists</li><li>Wedding Videographers</li><li>Wedding Officiants</li><li>Wedding Rentals</li><li>Wedding Photo Booths</li></ul></div>
  <div class="abs fcol" style="top:4683px;left:600px"><ul><li>Wedding Bands</li><li>Wedding Dresses &amp; Attire</li><li>Wedding Cakes</li><li>Wedding Limos / Transportation</li><li>Wedding Musicians / Ceremony Music</li></ul></div>
  <div class="abs fcol" style="top:4683px;left:860px"><ul><li>Wedding Decor &amp; Lighting</li><li>Wedding Invitations</li><li>Travel Agents</li><li>Wedding Jewelers</li><li>Wedding Favors &amp; Gifts</li></ul></div>
  <div class="abs fcol" style="top:4830px;left:125px"><h5>Digital Services</h5><ul><li>Logo Design</li><li>Portraits &amp; Caricatures</li><li>Video Editing</li><li>Invitation Design</li></ul></div>
  <div class="abs fcol" style="top:4869px;left:371px"><ul><li>Image Editing</li><li>Slideshow Videos</li><li>Speechwriting</li><li>Greeting Cards &amp; Videos</li></ul></div>
  <div class="abs fcol" style="top:4830px;left:600px"><h5>More from Brindlemoor</h5><ul><li>Brindlemoor Business</li><li>Careers</li><li>Press &amp; News</li><li>Partnership</li></ul></div>
  <div class="abs fcol" style="top:4830px;left:860px"><h5>Support</h5><ul><li>Help &amp; Support</li><li>Trust &amp; Safety</li><li>Selling on Brindlemoor</li><li>Buying on Brindlemoor</li></ul></div>

  <div class="abs bottombar">
    <span class="abs" style="left:125px;top:9px">© 2022 Brindlemoor. All Rights Reserved</span>
    <span class="abs" style="left:423px;top:9px">Privacy Policy &nbsp;&nbsp;|&nbsp;&nbsp; <span style="color:var(--magenta)">Terms of Service</span></span>
    <div class="social" style="left:970px;top:0;height:32px"><span></span></div>
    <div class="social active" style="left:1002px;top:0;height:32px"><span></span></div>
    <div class="social" style="left:1034px;top:0;height:32px"><span></span></div>
  </div>

</div>
</body>
</html>
```